Engineering firm Hero image for new web page

We are building a new webpage and need a Hero image. I have included a screen grab of the landing page showing where the image will be located. The company tag line (Engineering Tomorrow’s Automation) will be overlaid on the image so we need to be sure it works with the overlay.
We service a number of different industries, and we want something that is not overly specific so that if potential customers see something they don't recognize that we don't run them off. I have found several examples of a style that I think will work very well for us.
I want the Hero image to incorporate our competencies: Engineering, Automation, Integration, Robotics, Controls, Optimization.
There will be a follow on project to create a second image in the same theme which will highlight our industries served. Those will be: Food processing, Oil & Gas, Automotive, Aerospace, Medical, Contract Manufacturing. This image will be just below the hero and will be part of the “who we are section”

```html
<!DOCTYPE html>
<html lang="en">
<head>
<meta charset="utf-8">
<title>Vornex Systems — Engineering Tomorrow's Automation</title>
<link rel="stylesheet" href="https://fonts.googleapis.com/css2?family=Inter:wght@400;500;600;700;800&display=swap">
<style>
  :root {
    --navy-deep: #0a1620;
    --navy: #10222d;
    --crimson: #d7262a;
    --ring: #e8322c;
    --white: #ffffff;
    --text-soft: #e6e9ec;
    --hand-light: rgba(226, 230, 234, 0.55);
    --hand-mid: rgba(150, 162, 172, 0.28);
  }
  * { margin: 0; padding: 0; box-sizing: border-box; }
  html, body { width: 1200px; height: 968px; overflow: hidden; }
  body {
    font-family: "Inter", Arial, sans-serif;
    color: var(--white);
    background:
      radial-gradient(ellipse 520px 420px at 1200px 0px, rgba(190, 20, 28, 0.85), rgba(125, 13, 20, 0.45) 55%, transparent 100%),
      radial-gradient(ellipse 700px 500px at 900px 180px, rgba(125, 13, 20, 0.55), transparent 70%),
      radial-gradient(ellipse 420px 160px at 580px 390px, rgba(40, 90, 75, 0.3), transparent 70%),
      linear-gradient(180deg, var(--navy) 0%, var(--navy-deep) 60%, #0b1828 100%);
  }
  .page { position: relative; width: 1200px; height: 968px; }

  /* header */
  .brand {
    position: absolute; left: 244px; top: 12px;
    font-size: 40px; font-weight: 700; letter-spacing: -1px;
  }
  .main-nav a {
    position: absolute; top: 35px; white-space: nowrap;
    color: var(--white); text-decoration: none; font-size: 11px; font-weight: 400;
  }
  .btn {
    position: absolute; display: flex; align-items: center; justify-content: center;
    background: var(--crimson); color: var(--white); text-decoration: none;
    font-size: 11.5px; font-weight: 500; border-radius: 3px;
  }
  .btn-contact { left: 854px; top: 26px; width: 102px; height: 30px; }

  /* hero */
  .hero-hand {
    position: absolute; left: -60px; top: 230px; width: 560px; height: 230px;
    transform: rotate(-38deg);
    background:
      radial-gradient(closest-side at 72% 50%, var(--hand-light), rgba(200, 206, 212, 0.18) 55%, transparent 100%),
      radial-gradient(closest-side at 40% 50%, var(--hand-mid), transparent 100%);
    filter: blur(6px);
  }
  .hero-badge {
    position: absolute; left: 454px; top: 153px; width: 232px; height: 232px; border-radius: 50%;
    background: radial-gradient(circle at 50% 45%, #5a1014 0%, #3a0c10 55%, #1f0a0d 100%);
    box-shadow: 0 0 40px rgba(215, 38, 42, 0.35);
  }
  .badge-ring { position: absolute; inset: -6px; width: 244px; height: 244px; }
  .tagline {
    position: absolute; left: 0; right: 0; top: 57px; text-align: center;
    font-size: 20px; font-weight: 800; line-height: 25px; letter-spacing: 0.3px;
  }
  .badge-emblem { position: absolute; left: 84px; top: 138px; width: 64px; height: 64px; }

  .icon-disc {
    position: absolute; width: 62px; height: 62px; border-radius: 50%;
    background: radial-gradient(circle, #4a0e12 0%, #250b0e 100%);
    border: 2px solid var(--ring);
    box-shadow: 0 0 12px rgba(215, 38, 42, 0.45), inset 0 0 10px rgba(0,0,0,0.6);
  }
  .icon-disc::after {
    content: ""; position: absolute; right: -3px; bottom: 4px; width: 14px; height: 14px;
    border-right: 3px solid var(--white); border-bottom: 3px solid var(--white);
    border-radius: 0 0 14px 0; opacity: 0.85;
  }
  .icon-disc svg {
    position: absolute; left: 12px; top: 12px; width: 34px; height: 34px;
    fill: none; stroke: var(--white); stroke-width: 1.5; stroke-linecap: round; stroke-linejoin: round;
  }
  .icon-disc svg .accent { stroke: var(--ring); }
  .competency-label {
    position: absolute; font-size: 9px; font-weight: 600; letter-spacing: 0.2px; white-space: nowrap;
  }
  .industry-label {
    position: absolute; text-align: center; width: 120px; line-height: 11.5px;
    font-size: 9.4px; font-weight: 400; letter-spacing: 0.2px; white-space: nowrap;
  }

  /* who we are */
  .eyebrow {
    position: absolute; left: 614px; top: 569px;
    font-size: 11.5px; font-weight: 500; color: var(--crimson);
  }
  .section-title {
    position: absolute; left: 614px; top: 580px;
    font-size: 45px; font-weight: 700; letter-spacing: -0.5px;
  }
  .story {
    position: absolute; left: 620px; top: 645px; width: 370px;
    font-size: 10.3px; line-height: 20px; letter-spacing: -0.15px;
    text-align: justify; color: var(--text-soft);
  }
  .btn-learn { left: 618px; top: 863px; width: 102px; height: 30px; }
</style>
</head>
<body>
<div class="page">

  <header>
    <div class="brand">Vornex</div>
    <nav class="main-nav">
      <a href="#" style="left:554px">About Us</a>
      <a href="#" style="left:632px">Products</a>
      <a href="#" style="left:708px">Services</a>
      <a href="#" style="left:782px">News</a>
    </nav>
    <a class="btn btn-contact" href="#">Contact Us</a>
  </header>

  <section class="hero">
    <div class="hero-hand" role="img" aria-label="Robotic white hand reaching toward the tagline emblem"></div>

    <div class="hero-badge">
      <svg class="badge-ring" viewBox="0 0 244 244" aria-hidden="true">
        <circle cx="122" cy="122" r="116" fill="none" stroke="var(--ring)" stroke-width="4"
                stroke-dasharray="520 209" transform="rotate(-60 122 122)"/>
        <circle cx="122" cy="122" r="116" fill="none" stroke="var(--white)" stroke-width="3"
                stroke-dasharray="90 639" transform="rotate(15 122 122)" opacity="0.9"/>
      </svg>
      <h1 class="tagline">ENGINEERING<br>TOMORROW'S<br>AUTOMATION</h1>
      <svg class="badge-emblem" viewBox="0 0 64 64" fill="none" stroke="var(--white)" stroke-width="2" aria-hidden="true">
        <circle cx="32" cy="32" r="24" stroke-dasharray="6 4.05"  stroke-width="6"/>
        <circle cx="32" cy="32" r="20"/>
        <circle cx="32" cy="32" r="14" stroke="var(--ring)"/>
        <path d="M22 33 l6 -5 l5 3 l4 -3 l6 5 M27 36 l3 3 M31 35 l3 3 M35 34 l2 2" stroke="var(--ring)" stroke-linecap="round"/>
      </svg>
    </div>

    <ul class="competencies" style="list-style:none">
      <li><div class="icon-disc" style="left:621px;top:88px" role="img" aria-label="Engineering icon">
            <svg viewBox="0 0 34 34"><path d="M6 17 a11 11 0 0 1 22 0"/><path d="M4 17 h26"/><path d="M14 7 v6 M20 7 v6"/><path class="accent" d="M9 21 a8 8 0 0 0 16 0"/></svg></div>
          <span class="competency-label" style="left:690px;top:113px">ENGINEERING</span></li>
      <li><div class="icon-disc" style="left:697px;top:155px" role="img" aria-label="Automation icon">
            <svg viewBox="0 0 34 34"><path d="M6 13 a12 12 0 0 1 21 -3 M28 21 a12 12 0 0 1 -21 3"/><path d="M27 5 v5 h-5 M7 29 v-5 h5"/><circle cx="17" cy="17" r="6" stroke-dasharray="2.5 1.3" stroke-width="3"/><path class="accent" d="M15.5 14.5 l3.5 2.5 l-3.5 2.5 z"/></svg></div>
          <span class="competency-label" style="left:769px;top:180px">AUTOMATION</span></li>
      <li><div class="icon-disc" style="left:716px;top:244px" role="img" aria-label="Integration icon">
            <svg viewBox="0 0 34 34"><circle cx="12" cy="12" r="6" stroke-dasharray="2.6 1.6" stroke-width="3"/><circle cx="12" cy="12" r="2"/><circle class="accent" cx="22" cy="22" r="6" stroke-dasharray="2.6 1.6" stroke-width="3"/><circle class="accent" cx="22" cy="22" r="2"/></svg></div>
          <span class="competency-label" style="left:785px;top:269px">INTEGRATION</span></li>
      <li><div class="icon-disc" style="left:696px;top:331px" role="img" aria-label="Robotics icon">
            <svg viewBox="0 0 34 34"><path d="M8 30 h14 M12 30 l3 -6 h0"/><path d="M15 24 l-5 -12 l12 -5"/><circle cx="10" cy="12" r="2"/><circle cx="15" cy="24" r="2"/><path class="accent" d="M22 7 l4 2 M22 7 l3 -3"/></svg></div>
          <span class="competency-label" style="left:767px;top:356px">ROBOTICS</span></li>
      <li><div class="icon-disc" style="left:622px;top:396px" role="img" aria-label="Controls icon">
            <svg viewBox="0 0 34 34"><path d="M11 12 a6 6 0 0 1 12 0 M7 12 a10 10 0 0 1 20 0"/><path class="accent" d="M15 13 v10 l-3 -2 l-2 2 l5 7 h8 l1 -8 l-6 -2 v-7 a1.5 1.5 0 0 0 -3 0"/></svg></div>
          <span class="competency-label" style="left:691px;top:421px">CONTROLS</span></li>
    </ul>
  </section>

  <section class="who-we-are">
    <ul class="industries" style="list-style:none">
      <li><div class="icon-disc" style="left:251px;top:615px" role="img" aria-label="Food processing icon">
            <svg viewBox="0 0 34 34"><path d="M9 30 v-18 h16 v18 z M7 12 h20 M11 8 h12 v4"/><circle class="accent" cx="14" cy="18" r="1.5"/><circle class="accent" cx="20" cy="18" r="1.5"/><circle class="accent" cx="14" cy="24" r="1.5"/><circle class="accent" cx="20" cy="24" r="1.5"/></svg></div>
          <span class="industry-label" style="left:223px;top:690px">FOOD<br>PROCESSING</span></li>
      <li><div class="icon-disc" style="left:374px;top:615px" role="img" aria-label="Oil and gas icon">
            <svg viewBox="0 0 34 34"><path d="M6 30 h22 M11 30 l6 -20 l6 20 M13 23 h8 M14 18 h6"/><path d="M6 8 h20 l3 4"/><circle class="accent" cx="8" cy="25" r="3"/></svg></div>
          <span class="industry-label" style="left:345px;top:690px">OIL &amp; GAS</span></li>
      <li><div class="icon-disc" style="left:497px;top:615px" role="img" aria-label="Automotive icon">
            <svg viewBox="0 0 34 34"><path d="M4 23 v-4 l4 -1 l4 -5 h9 l4 5 l5 1 v4 h-3 M10 23 h12"/><circle class="accent" cx="10" cy="24" r="3"/><circle class="accent" cx="24" cy="24" r="3"/></svg></div>
          <span class="industry-label" style="left:468px;top:690px">AUTOMOTIVE</span></li>
      <li><div class="icon-disc" style="left:251px;top:741px" role="img" aria-label="Aerospace icon">
            <svg viewBox="0 0 34 34"><path d="M17 4 c5 5 5 13 3 19 h-6 c-2 -6 -2 -14 3 -19 z"/><circle cx="17" cy="13" r="2"/><path d="M14 18 l-4 6 h4 M20 18 l4 6 h-4"/><path class="accent" d="M15 26 l2 5 l2 -5"/></svg></div>
          <span class="industry-label" style="left:222px;top:816px">AEROSPACE</span></li>
      <li><div class="icon-disc" style="left:373px;top:741px" role="img" aria-label="Medical icon">
            <svg viewBox="0 0 34 34"><rect x="6" y="8" width="22" height="20" rx="2"/><path class="accent" d="M17 12 v12 M11 18 h12"/></svg></div>
          <span class="industry-label" style="left:344px;top:816px">MEDICAL</span></li>
      <li><div class="icon-disc" style="left:496px;top:741px" role="img" aria-label="Contract manufacturing icon">
            <svg viewBox="0 0 34 34"><path d="M6 20 v-12 h6 v4 h6 v-4 h10 v12"/><path d="M9 12 v4 M24 12 v4 M20 12 v4"/><path class="accent" d="M5 24 l6 -2 l5 3 l5 -3 l8 2 M13 27 l3 2 l3 -2"/></svg></div>
          <span class="industry-label" style="left:467px;top:816px">CONTRACT<br>MANUFACTURING</span></li>
    </ul>

    <p class="eyebrow">OUR STORY</p>
    <h2 class="section-title">Who we are ?</h2>
    <p class="story">Vornex Systems is an integration, automation, and machine design company based out of Austin, Texas that focuses on providing services to update and improve existing machines and processes as well as develop new process equipment. Vornex is comprised of a collection of electrical and mechanical engineers with an extensive background in multiple industries that include: machine tools, nano-technology, nuclear power, semiconductor, oil and gas, food and beverage, packaging and medical. It is this diverse expertise that allows us to draw on many disciplines to tailor the most efficient and cost effective solution to a customer’s need. Using the latest in hardware and software, Vornex Systems will improve your up-time, process, and performance.</p>
    <a class="btn btn-learn" href="#">Learn More</a>
  </section>

</div>
</body>
</html>
```